The Harwood Bellamy Firm

We are a real estate and business acquisition services company that provides consulting services to large companies and individuals. The company provided nationwide services to companies looking to expand through opening new locations or buying other companies in their field. We work very close with attorneys, accountants, banks/financial institutions and high level executives and business owners.

Target Market(s)

CEO, VP, business owners and bankers.

Industry/Entity Type

Real Estate

Requirements
Must have
• I am looking for a design that looks very professional and has a classic, trustworthy, professional feeling. I want the letterhead and return address to look formal and official so this it is not tossed out as junk mail. HB or HBF can be used in a logo style part but that is not required. Our tag line is "Real Estate and Business Acquisition Services". This should be on the letter head but not on the return address. It does not need a lot of color but I will leave that to your tasteful choice. It should be rich and formal looking.
Should not have
• I do not want anything that looks like a cartoon drawing or figure. Use font that gives a strong trustworthy look. We are not a law firm so no scales or gavels. A law firm sort of look or feel is OK.

```html
<!DOCTYPE html>
<html lang="en">
<head>
<meta charset="utf-8">
<title>The Harwood Bellamy Firm – Business Card</title>
<link rel="stylesheet" href="https://fonts.googleapis.com/css2?family=EB+Garamond:wght@400&family=Lato:wght@400&display=swap">
<style>
  :root {
    --backdrop: #e7e4df;
    --card: #ffffff;
    --ink: #1c1c1c;
    --rule: #6b6b6b;
    --ornament-tone: #d9d9d9;
  }
  html, body {
    margin: 0;
    padding: 0;
    width: 1200px;
    height: 790px;
    overflow: hidden;
    background: var(--backdrop);
  }
  .business-card {
    position: absolute;
    left: 75px;
    top: 95px;
    width: 1050px;
    height: 600px;
    background: var(--card);
    box-shadow: 0 6px 24px rgba(0, 0, 0, 0.12);
  }
  .firm-name {
    position: absolute;
    left: 200px;
    width: 660px;
    top: 140px;
    margin: 0;
    font-family: "EB Garamond", Georgia, serif;
    font-weight: 400;
    font-size: 64px;
    line-height: 1;
    color: var(--ink);
    text-align: center;
    white-space: nowrap;
    letter-spacing: -0.5px;
  }
  .firm-name .article {
    font-size: 46px;
  }
  .card-lines {
    position: absolute;
    left: 0;
    top: 0;
    width: 1050px;
    height: 600px;
  }
  .return-address {
    position: absolute;
    left: 532px;
    top: 428px;
    margin: 0;
    font-family: "Lato", "Helvetica Neue", Arial, sans-serif;
    font-style: normal;
    font-size: 29px;
    line-height: 44px;
    color: var(--ink);
    white-space: nowrap;
  }
</style>
</head>
<body>
  <div class="business-card">
    <svg class="card-lines" viewBox="0 0 1050 600" aria-hidden="false">
      <line class="name-rule" x1="200" y1="232" x2="860" y2="218" stroke="var(--rule)" stroke-width="2"/>
      <line class="accent-rule" x1="335" y1="272" x2="725" y2="268" stroke="var(--rule)" stroke-width="2"/>
      <rect class="ornament" x="480" y="252" width="100" height="36" fill="var(--ornament-tone)" role="img" aria-label="Ornament of three linked outline diamonds"/>
      <line class="address-divider" x1="502" y1="428" x2="502" y2="545" stroke="var(--rule)" stroke-width="2"/>
    </svg>
    <h1 class="firm-name"><span class="article">The</span> Harwood Bellamy Firm</h1>
    <address class="return-address">
      4120 Ridgeline Avenue, Suite 210<br>
      Brentwood, TN&nbsp; 37027
    </address>
  </div>
</body>
</html>
```